Electrical and Audio Visual Business Card Design

We need a business card design for our company called T.O.K.L.E (Tobin's Optic Kinetic & Lumen Engineering PtyLtd).
We provide Electrical Services as well as Audio Visual demands.
Services provided:
Electrical repairs
Additions
Extensions
Audio Visual solutions
Data
Smoke alarms
TV antennas
Automation
Updates

Also looking for a company logo. Uniforms are black if this helps.

Industry/Entity Type

Business

Contact Information for Business Card

Tobin Lumen Pty Ltd
Martin Gollisby
58 Fenwick Rd,
Harlow Vale, 2871
mjgollisby@pelicanmail.com

Logo Text

T.O.K.L.E.

Requirements
Must have
• Please can we have a double sided card. Showing our services on the back. Can I also have the number 0451296847. Can we also change email address to mgollisby@tokle.net.au

```html
<!DOCTYPE html>
<html lang="en">
<head>
<meta charset="utf-8">
<title>Tobin Lumen Pty Ltd – Business Card</title>
<link rel="stylesheet" href="https://fonts.googleapis.com/css2?family=Itim&family=Crimson+Text:wght@400&display=swap">
<style>
  :root {
    --lime: #88ff00;
    --mist: #e8ecea;
    --ink: #111111;
    --frame: #000000;
    --page: #ffffff;
  }
  * { box-sizing: border-box; margin: 0; padding: 0; }
  html, body {
    width: 1200px; height: 357px; overflow: hidden;
    background: var(--page);
  }
  .sheet { position: relative; width: 1200px; height: 357px; }
  .card-frame {
    position: absolute; top: 1px; width: 583px; height: 354px;
    border: 2px solid var(--frame); background: var(--page);
  }
  .card-frame--back { left: 5px; }
  .card-frame--front { left: 612px; }
  .card-face {
    position: absolute; top: 22px; left: 19px; width: 540px; height: 309px;
    overflow: hidden;
  }
  .card-back { background: var(--lime); }
  .card-front { background: var(--mist); }

  .company-title {
    position: absolute; left: 36px; top: 150px;
    font-family: "Itim", cursive; font-weight: 400; font-size: 21px; color: var(--ink);
    white-space: nowrap;
  }
  .services {
    position: absolute; left: 36px; top: 213px;
    font-family: "Crimson Text", serif; font-size: 15.5px; line-height: 20px;
    color: var(--ink);
  }

  .curve { position: absolute; inset: 0; width: 100%; height: 100%; }

  .brand {
    position: absolute; left: 36px; top: 90px;
    font-family: "Itim", cursive; font-size: 16px; color: var(--ink);
    white-space: nowrap;
  }

  .person-name {
    position: absolute; left: 0; width: 490px; top: 150px; text-align: center;
    font-family: "Crimson Text", serif; font-size: 23px; color: var(--ink);
  }
  .name-rule {
    position: absolute; left: 196px; top: 185px; width: 102px; height: 2px;
    background: var(--ink);
  }
  .contact {
    position: absolute; left: 26px; top: 193px;
    font-family: "Crimson Text", serif; font-size: 15.5px; line-height: 20px;
    color: var(--ink);
  }
  .contact-line { display: flex; align-items: center; gap: 6px; }
  .contact-line svg { width: 12px; height: 12px; flex: none; }
  .address {
    position: absolute; left: 0; width: 500px; top: 265px; text-align: center;
    font-family: "Crimson Text", serif; font-size: 15.5px; color: var(--ink);
  }
</style>
</head>
<body>
<div class="sheet">

  <div class="card-frame card-frame--back">
    <div class="card-face card-back">
      <h1 class="company-title">Tobin's Optic Kinetic &amp; Lumen Engineering PtyLtd</h1>
      <div class="services">
        <p>Services provided:</p>
        <p>Electrical repairs, Additions, Extensions, Audio Visual solutions</p>
        <p>Data, Smoke alarms, TV antennas, Automation</p>
      </div>
    </div>
  </div>

  <div class="card-frame card-frame--front">
    <div class="card-face card-front">
      <svg class="curve" viewBox="0 0 540 309" preserveAspectRatio="none" aria-hidden="true">
        <path d="M 452 0 C 405 12, 408 85, 440 135 C 485 205, 480 285, 245 309 L 540 309 L 540 0 Z" fill="var(--lime)"/>
      </svg>

      <p class="brand">Tobin Lumen Pty Ltd</p>

      <p class="person-name">Martin Gollisby</p>
      <span class="name-rule"></span>

      <div class="contact">
        <p class="contact-line">
          <svg viewBox="0 0 12 12" aria-label="Phone"><path d="M1 4 Q6 0 11 4 L9 5.5 L8 4.5 L4 4.5 L3 5.5 Z M3 6 L9 6 L10 10 L2 10 Z" fill="var(--ink)"/></svg>
          0451296847
        </p>
        <p class="contact-line">
          <svg viewBox="0 0 12 12" aria-label="Email"><rect x="1" y="3" width="10" height="7" rx="1.5" fill="var(--ink)"/><path d="M1.5 4 L6 7 L10.5 4" stroke="var(--mist)" stroke-width="0.8" fill="none"/></svg>
          mgollisby@tokle.net.au
        </p>
      </div>

      <p class="address">58 Fenwick Rd, Harlow Vale, 2871</p>
    </div>
  </div>

</div>
</body>
</html>
```